'Ormel Property Development' Business Card

Business Card Features:

High Quality (potentially textured) thick card - preference is white textured card

Logo (supplied)

We plan to use the vertical logo as the main logo. But i am happy for people to use either if they find it works better for the design of the card.

The building icon and also the insert to the 'E' is in a metallic finish, i think this should be finished in a metallic embossed or raised style.
Updates

Please note i have attached both a horizontal and Vertical Logo for your reference. We plan to use the vertical logo as the main logo. But i am happy for people to use either if they find it works better for the design of the card.

Please note i am considering having the cards made on stainless steel. This introduces the option of having cut outs in the card and etching or printing for the design. If you have a good concept for this please submit.

http://www.tinquarry.example/black-metal-cards# this is a site that makes the metal cards to offer some direction . . . . Please note i am basic the selection o the best design, if that means normal print cards on paper then this is what i will choose. But there are some great options with the metal. Thanks.

Industry/Entity Type

Building

Requirements
Must have
• Helvetica font to details side of card - logo as supplied to opposite side.

Card Details:

Darrow Pketts
Managing Director

+61 487 263 518
+61 3 6172 4809

PO Box 73
Bentleigh, VIC 3024

darrow@ormel.example

www.ormel.example

```html
<!DOCTYPE html>
<html lang="en">
<head>
<meta charset="utf-8">
<title>Ormel Property Development – Business Card</title>
<link rel="stylesheet" href="https://fonts.googleapis.com/css2?family=Arimo:wght@400;700&display=swap">
<style>
  :root {
    --backdrop: #6e5441;
    --card-dark: #1d1d1e;
    --card-mid: #2b2b2c;
    --card-band: #3a3a3b;
    --metal: #b9b9bb;
    --ink-white: #ffffff;
    --ink-soft: #e6e6e6;
    --rule: #7a7a7d;
  }
  * { box-sizing: border-box; margin: 0; padding: 0; }
  html, body {
    width: 1200px; height: 800px; overflow: hidden;
    background: var(--backdrop);
    font-family: "Arimo", "Helvetica Neue", Helvetica, Arial, sans-serif;
  }
  .stage { position: relative; width: 1200px; height: 800px; }

  .card {
    position: absolute;
    width: 500px; height: 286px;
    border-radius: 4px;
    background: radial-gradient(ellipse at 40% 30%, var(--card-mid) 0%, var(--card-dark) 75%);
    box-shadow: 0 3px 0 #111, 0 6px 0 #161616, 0 9px 0 #111, 0 14px 24px rgba(0,0,0,.45);
    overflow: hidden;
  }

  /* Front: logo side */
  .card--front { left: 90px; top: 100px; }
  .front-mark {
    position: absolute; inset: 0;
    display: flex; flex-direction: column; align-items: center; justify-content: center;
    gap: 6px; color: var(--metal);
  }
  .front-mark__square { width: 46px; height: 46px; background: var(--metal); margin-bottom: 10px; }
  .front-mark__name { font-size: 52px; font-weight: 400; letter-spacing: 4px; line-height: 1; }
  .front-mark__sub { font-size: 16px; font-weight: 400; letter-spacing: 1px; }

  /* Back: details side */
  .card--back { left: 610px; top: 410px; }
  .band {
    position: absolute; left: 0; right: 0; top: 112px; height: 66px;
    background: linear-gradient(180deg, var(--card-band), #333334);
  }
  .back-logo {
    position: absolute; left: 34px; top: 30px;
    display: flex; align-items: center; gap: 14px; color: var(--metal);
  }
  .back-logo__square { width: 56px; height: 56px; background: var(--metal); }
  .back-logo__rule { width: 1px; height: 74px; background: var(--rule); }
  .back-logo__text { display: flex; flex-direction: column; gap: 4px; }
  .back-logo__name { font-size: 40px; letter-spacing: 3px; line-height: 1; }
  .back-logo__sub { font-size: 12px; letter-spacing: .5px; }

  .person {
    position: absolute; right: 26px; top: 120px; text-align: right; color: var(--ink-white);
  }
  .person__name { font-size: 28px; font-weight: 700; line-height: 1.05; }
  .person__role { font-size: 18px; font-weight: 400; color: var(--ink-soft); }

  .contacts {
    position: absolute; left: 34px; top: 192px; list-style: none;
    color: var(--ink-white); font-size: 12.5px; font-weight: 700;
  }
  .contacts li { display: flex; align-items: center; gap: 7px; height: 17px; white-space: nowrap; }
  .contacts svg { width: 12px; height: 12px; flex: none; }
</style>
</head>
<body>
<main class="stage">

  <section class="card card--front" aria-label="Card front">
    <div class="front-mark">
      <span class="front-mark__square"></span>
      <span class="front-mark__name">ORMEL</span>
      <span class="front-mark__sub">Property Development</span>
    </div>
  </section>

  <section class="card card--back" aria-label="Card back">
    <div class="band"></div>

    <div class="back-logo">
      <span class="back-logo__square"></span>
      <span class="back-logo__rule"></span>
      <span class="back-logo__text">
        <span class="back-logo__name">ORMEL</span>
        <span class="back-logo__sub">Property Development</span>
      </span>
    </div>

    <div class="person">
      <p class="person__name">Darrow Pketts</p>
      <p class="person__role">Managing Director</p>
    </div>

    <ul class="contacts">
      <li>
        <svg viewBox="0 0 12 12" fill="none" stroke="currentColor" stroke-width="1.2"><rect x="3" y="0.8" width="6" height="10.4" rx="1"/><line x1="5" y1="9.5" x2="7" y2="9.5"/></svg>
        +61 487 263 518
      </li>
      <li>
        <svg viewBox="0 0 12 12" fill="currentColor"><path d="M2.5 1 L4.5 1 L5.3 3.6 L4 4.6 C4.7 6.1 5.9 7.3 7.4 8 L8.4 6.7 L11 7.5 L11 9.5 C11 10.3 10.3 11 9.5 11 C5.4 11 1 6.6 1 2.5 C1 1.7 1.7 1 2.5 1 Z"/></svg>
        +61 3 6172 4809
      </li>
      <li>
        <svg viewBox="0 0 12 12" fill="none" stroke="currentColor" stroke-width="1.3"><path d="M6 11 C3 7.5 2 5.8 2 4.3 A4 4 0 0 1 10 4.3 C10 5.8 9 7.5 6 11 Z"/><circle cx="6" cy="4.4" r="1.4"/></svg>
        PO BOX 73 Bentleigh, VIC 3024
      </li>
      <li>
        <svg viewBox="0 0 12 12" fill="none" stroke="currentColor" stroke-width="1.2"><rect x="0.8" y="2.3" width="10.4" height="7.4"/><path d="M0.8 2.3 L6 6.6 L11.2 2.3"/></svg>
        darrow@ormel.example
      </li>
      <li>
        <svg viewBox="0 0 12 12" fill="none" stroke="currentColor" stroke-width="1.2"><rect x="0.8" y="1.2" width="10.4" height="7"/><line x1="6" y1="8.2" x2="6" y2="10.5"/><line x1="3.5" y1="10.8" x2="8.5" y2="10.8"/></svg>
        www.ormel.example
      </li>
    </ul>
  </section>

</main>
</body>
</html>
```